Collagen Tub Packaging Design for a New Brand

PLEASE DON'T SEND ANY NEW DESIGNS WE JUST HAVE TO DECIDE WITH MY PARTNERS THANKS A LOT.
I've created a very detailed document & design examples of what we like in certain designs and what we don't.

There are 3 documents:
1- Brief for the Design (please read it before designing)
2- Brand Design Examples that we like (and why we like them)
3- Die cut for the packaging design. This will be it's dimensions.

We are NOT looking for someone to micro-manage. In contrast, we want someone to help us express our ideas better with their design. Nothing I say in these briefs are there to limit the creativity of the designer, because if we knew exactly what we wanted we would do it ourselves but we trust the designer's expertise in this packaging design.

In short: We want our brand to feel premium, high-quality & trust worthy with it's design not feeling very busy or bloated. We don't have a logo source file, but you'll get the idea of what we want when you see it).

Let me know if you have any further questions, will answer each question real fast.

Thanks.

Target Market(s)

Pretty much everyone above 25+ in Turkey because nearly all of them are using are collagens so our audience is wild.

Industry/Entity Type

Collagen - Health, Wellness & Supplements

Font styles to use
Serif
Sans Serif

Colors

Designer to choose colors to be used in the design.

Requirements
Must have
• Our design should be distinct, a design style which everyone can identify from 10 meters away if they know the product. This is a MUST have for us. It's up to designer to achieve it. This can be just a simple color palette aswell.
Should not have
• It shouldn't feel bloated and very busy. Please avoid very detailed icons (as a rule of thumb, if you can make it work great)

```html
<!DOCTYPE html>
<html lang="en">
<head>
<meta charset="utf-8">
<title>Lumora Hydrolyzed Collagen Peptides – Tub Label</title>
<link rel="stylesheet" href="https://fonts.googleapis.com/css2?family=Libre+Baskerville:wght@700&family=Roboto:wght@400;500&display=swap">
<style>
  :root {
    --page-bg: #efefef;
    --label-grey: #d9d9d9;
    --label-grey-light: #e6e6e6;
    --brand-navy: #1b2f5e;
    --band-blue-dark: #1d5f8f;
    --band-blue: #1b79ab;
    --pattern-dark: #0f3d8a;
    --pattern-light: #2b86d6;
    --white: #ffffff;
    --text-dark: #1a1a1a;
    --box-border: #2265a0;
  }
  * { box-sizing: border-box; margin: 0; padding: 0; }
  html, body {
    width: 1200px; height: 800px; overflow: hidden;
    background: var(--page-bg);
    font-family: "Roboto", Arial, sans-serif;
  }
  .label {
    position: absolute; left: 20px; top: 213px;
    width: 1160px; height: 374px;
    background: var(--white);
    overflow: hidden;
  }
  .label__cap-band {
    position: absolute; left: 0; top: 0; width: 100%; height: 40px;
    background: linear-gradient(180deg, #d2d2d2, var(--label-grey-light));
    border-top: 1px solid #bdbdbd;
  }
  .label__pattern {
    position: absolute; left: 0; top: 40px; width: 126px; height: 313px;
    background: linear-gradient(160deg, var(--pattern-dark) 0%, var(--pattern-light) 45%, var(--pattern-dark) 70%, #1c6cc4 100%);
  }
  .label__brand-area {
    position: absolute; left: 126px; top: 40px; right: 0; height: 103px;
    background: var(--white);
  }
  .label__band {
    position: absolute; left: 126px; top: 143px; right: 0; height: 210px;
    background: linear-gradient(180deg, var(--band-blue-dark), var(--band-blue));
  }
  .label__foot-line {
    position: absolute; left: 0; top: 353px; width: 100%; height: 9px;
    background: var(--label-grey-light);
  }
  .label__foot-band {
    position: absolute; left: 0; top: 362px; width: 100%; height: 12px;
    background: var(--band-blue);
  }
  .brand {
    position: absolute; left: 196px; top: 70px;
    display: flex; align-items: center; gap: 8px;
  }
  .brand__dot {
    width: 16px; height: 16px; border: 2px solid var(--brand-navy); border-radius: 50%;
  }
  .brand__name {
    font-family: "Roboto", Arial, sans-serif; font-weight: 500;
    font-size: 42px; color: var(--brand-navy); letter-spacing: 1px; line-height: 1;
  }
  .product-type {
    position: absolute; left: 151px; top: 150px;
    font-family: "Libre Baskerville", Georgia, serif; font-weight: 700;
    font-size: 19px; color: var(--white);
  }
  .product-name {
    position: absolute; left: 148px; top: 170px;
    font-family: "Roboto", Arial, sans-serif; font-weight: 400;
    font-size: 60px; line-height: 1; color: var(--white); letter-spacing: 0.5px;
  }
  .product-sub {
    position: absolute; left: 151px; width: 285px; top: 233px; text-align: right;
    font-family: "Libre Baskerville", Georgia, serif; font-weight: 700;
    font-size: 18px; color: var(--white);
  }
  .tagline {
    position: absolute; left: 183px; top: 266px; width: 216px; height: 19px;
    background: var(--white); border-radius: 10px;
    font-size: 14.5px; line-height: 19px; text-align: center; color: var(--text-dark);
  }
  .benefits {
    position: absolute; left: 196px; top: 303px;
    display: flex; gap: 18px; list-style: none;
  }
  .benefit {
    width: 34px; display: flex; flex-direction: column; align-items: center;
    font-size: 8.5px; color: var(--white);
  }
  .benefit svg { width: 32px; height: 32px; display: block; margin-bottom: 3px; }
  .info-box {
    position: absolute; left: 612px; top: 63px; width: 453px; height: 267px;
    background: var(--white); border: 2px solid var(--box-border);
    padding: 24px 26px 10px 20px;
    font-size: 7.4px; line-height: 9.9px; color: var(--text-dark); text-align: justify;
  }
</style>
</head>
<body>
  <main class="label">
    <div class="label__cap-band"></div>
    <div class="label__pattern" role="img" aria-label="Faceted blue geometric crystal pattern"></div>
    <div class="label__brand-area"></div>
    <div class="label__band"></div>
    <div class="label__foot-line"></div>
    <div class="label__foot-band"></div>

    <div class="brand">
      <span class="brand__dot"></span>
      <span class="brand__name">Lumora</span>
    </div>

    <p class="product-type">Hdyrolyzed</p>
    <h1 class="product-name">COLLOGEN</h1>
    <p class="product-sub">PEPTIDES</p>
    <p class="tagline">Empowering Radiant Revival!</p>

    <ul class="benefits">
      <li class="benefit">
        <svg viewBox="0 0 32 32" fill="none" stroke="#fff" stroke-width="1.4"><circle cx="16" cy="16" r="14.5"/><path d="M16 8c-3 4-5 7-5 10a5 5 0 0 0 10 0c0-3-2-6-5-10z"/></svg>
        Skin
      </li>
      <li class="benefit">
        <svg viewBox="0 0 32 32" fill="none" stroke="#fff" stroke-width="1.4"><circle cx="16" cy="16" r="14.5"/><path d="M11 8c-2 5 2 7 0 12s1 5 1 5M16 7c-2 5 2 8 0 13s1 5 1 5M21 8c-2 5 2 7 0 12s1 5 1 5"/></svg>
        Hair
      </li>
      <li class="benefit">
        <svg viewBox="0 0 32 32" fill="none" stroke="#fff" stroke-width="1.4"><circle cx="16" cy="16" r="14.5"/><rect x="12" y="12" width="6" height="12" rx="3"/><path d="M21 7v5M18.5 9.5h5M24 14v3M22.5 15.5h3"/></svg>
        Nails
      </li>
      <li class="benefit">
        <svg viewBox="0 0 32 32" fill="none" stroke="#fff" stroke-width="1.6"><circle cx="16" cy="16" r="14.5"/><path d="M20 8l-6 8 5 8"/><circle cx="14" cy="16" r="2"/></svg>
        Joints
      </li>
    </ul>

    <section class="info-box">
      <p>Hydrolyzed collagen peptides are short protein chains that dissolve easily in water, coffee, juice or smoothies without changing taste or texture. Each serving supplies amino acids such as glycine, proline and hydroxyproline that support the natural structure of skin, hair, nails and connective tissue. Our peptides are sourced from carefully selected bovine hides and processed at low temperatures to keep them clean and neutral.</p>
      <p>Directions: mix one level scoop (10 g) into 200 ml of your favourite cold or warm drink once a day. Stir well until fully dissolved. For best results use daily for at least eight weeks.</p>
      <p>Ingredients: hydrolyzed bovine collagen peptides (type I and III). Contains no added sugar, gluten, dairy, artificial colours or preservatives. Produced in a facility that follows good manufacturing practice and is checked batch by batch for purity and quality.</p>
      <p>Warnings: this product is a food supplement and should not replace a varied, balanced diet and healthy lifestyle. Do not exceed the recommended daily dose. Consult your doctor before use if you are pregnant, nursing or taking medication.</p>
      <p>Storage: keep the lid tightly closed and store in a cool, dry place away from direct sunlight. Keep out of reach of children. Use within three months of opening. Net weight: 300 g, 30 servings.</p>
      <p>Best before and batch number: see bottom of the tub.</p>
    </section>
  </main>
</body>
</html>
```